Business card for a "family office" company

Please provide professional looking business card designs, incorporating the attached logo and below details. Harrowmere Holdings Pty Ltd is a family office / financial investment company. We are looking for a modern, professional and contemporary card design.

Industry/Entity Type

Finance

Contact Information for Business Card

Name: Dean Mollick
Title: Director
Company: Harrowmere Holdings Pty Ltd
Email: harrowdean@quillnet.example
Mobile: 0462 735 418
Address: 4/312 Barnaby Parade, Fernhollow WA 6994, Australia

Requirements
Must have
• All details above and the logo. logo only on back side. incorporate colours of logo
Nice to have
• up to you
Should not have
• ?

```html
<!DOCTYPE html>
<html lang="en">
<head>
<meta charset="utf-8">
<title>Harrowmere Holdings – Business Card</title>
<link href="https://fonts.googleapis.com/css2?family=Roboto:wght@400;500;700&display=swap" rel="stylesheet">
<style>
  :root {
    --navy: #25277a;
    --card: #ffffff;
    --backdrop: #e6e7ea;
    --rule: #c9cadb;
  }
  * { box-sizing: border-box; margin: 0; padding: 0; }
  html, body {
    width: 1200px;
    height: 1200px;
    overflow: hidden;
    background: var(--backdrop);
    font-family: "Roboto", Arial, sans-serif;
    color: var(--navy);
  }
  .canvas {
    position: relative;
    width: 1200px;
    height: 1200px;
  }
  .card {
    position: absolute;
    left: 220px;
    width: 760px;
    height: 430px;
    background: var(--card);
    box-shadow: 0 6px 18px rgba(0,0,0,0.12);
  }
  .card--front {
    top: 120px;
    border-bottom: 10px solid var(--navy);
    display: flex;
    align-items: center;
    justify-content: center;
  }
  .card--back {
    top: 650px;
    display: flex;
    flex-direction: column;
    align-items: center;
    padding-top: 92px;
    text-align: center;
  }
  .brand {
    display: flex;
    flex-direction: column;
    align-items: center;
    gap: 26px;
  }
  .brand__square {
    width: 120px;
    height: 120px;
    background: var(--navy);
  }
  .brand__name {
    font-size: 38px;
    font-weight: 500;
    letter-spacing: 5px;
    text-transform: uppercase;
    color: var(--navy);
    line-height: 1;
    white-space: nowrap;
  }
  .holder__name {
    font-size: 27px;
    font-weight: 700;
    font-variant: small-caps;
    letter-spacing: 0.5px;
  }
  .holder__title {
    font-size: 17px;
    font-weight: 500;
    letter-spacing: 1px;
    margin-top: 2px;
  }
  .holder__company {
    font-size: 15px;
    font-weight: 400;
    letter-spacing: 2px;
    margin-top: 4px;
    text-transform: uppercase;
  }
  .divider {
    width: 360px;
    height: 1px;
    margin: 20px 0 34px;
    background: linear-gradient(90deg, transparent, var(--rule), transparent);
  }
  .icons {
    display: flex;
    gap: 6px;
    margin-bottom: 8px;
  }
  .icons svg { width: 24px; height: 24px; }
  .contact {
    font-size: 18px;
    line-height: 1.3;
    color: var(--navy);
  }
</style>
</head>
<body>
<main class="canvas">
  <section class="card card--front">
    <div class="brand">
      <span class="brand__square"></span>
      <span class="brand__name">Harrowmere Holdings</span>
    </div>
  </section>

  <section class="card card--back">
    <div class="holder__name">Dean Mollick</div>
    <div class="holder__title">DIRECTOR</div>
    <div class="holder__company">Harrowmere Holdings Pty Ltd</div>
    <div class="divider"></div>
    <div class="icons">
      <svg viewBox="0 0 24 24" aria-label="Mobile">
        <circle cx="12" cy="12" r="10.5" fill="none" stroke="#25277a" stroke-width="1.5"/>
        <rect x="8.5" y="6" width="7" height="12" rx="1.2" fill="none" stroke="#25277a" stroke-width="1.5"/>
        <line x1="11" y1="16" x2="13" y2="16" stroke="#25277a" stroke-width="1.2"/>
      </svg>
      <svg viewBox="0 0 24 24" aria-label="Email">
        <circle cx="12" cy="12" r="10.5" fill="none" stroke="#25277a" stroke-width="1.5"/>
        <rect x="6.5" y="8" width="11" height="8" fill="#25277a"/>
        <polyline points="6.5,8 12,12.5 17.5,8" fill="none" stroke="#fff" stroke-width="1.2"/>
      </svg>
      <svg viewBox="0 0 24 24" aria-label="Address">
        <circle cx="12" cy="12" r="10.5" fill="none" stroke="#25277a" stroke-width="1.5"/>
        <path d="M12 18 C9 14.5 8 13 8 11 a4 4 0 0 1 8 0 c0 2-1 3.5-4 7z" fill="#25277a"/>
        <circle cx="12" cy="11" r="1.5" fill="#fff"/>
      </svg>
    </div>
    <div class="contact">
      0462 735 418<br>
      harrowdean@quillnet.example<br>
      4/312 Barnaby Parade, Fernhollow<br>
      WA 6994, Australia
    </div>
  </section>
</main>
</body>
</html>
```